Hotdogs & Burgers restaurant needs a new menu design

We need a new menu design for our restaurant "Wurmelo". Wurmelo is a fast food specialized in hotdogs and burgers.We are looking for a simple easy menu design that walk through our customer to order the sandwich ==> the fries =>> the sides and the drinks. Wurmelo Menu:* Sandwiches**Hotdogs Our special fresh grilled hotdog served on fresh buns (Regular – 1.300 OMR / Franks – 2.000 OMR)*** DoganzaLettuce, tomato, jalapeno, pickle, onion, corn, chips, cheese, ketchup, mayo, mustard*** PepperBell pepper, onion, sweet chili sauce, avocado*** Chili FlamesChili carne, cheddar cheese, honey mustard*** ChicagoTomato, pickle, red onion, sweet relish, mustard*** New YorkGrilled onion, beef bacon, barbecue sauce, chili mustard*** Egg & CheeseOmelet, cheese, ketchup, mayo, mustard** Burgers 100% all natural beef & freshly ground, 100 grams each patty served on fresh buns.(Single patty - 2.000 OMR / double patty - 2.500 OMR)*** Sweet Beef BurgerBeef bacon, cheese, lettuce, tomato, pickle.*** Cheese Beef BurgerCheese, pickle, Wurmelo sauce.*** Mexican Beef BurgerGuacamole sauce, red onion, lettuce, tomato, Wurmelo sauce.*** Chicken BurgerFried chicken patty, lettuce, tomato, ranch sauce, Wurmelo sauce== ToppingsExtra veggies 0.100 OMRExtra cheese 0.200 OMRExtra beef Bacon 0.400 OMRExtra patty 0.500 OMR*Fries**Regular 0.600 OMR**Crispy 0.800 OMR**Wedges 0.800 OMR**Chili fries 1.500 OMRTopped with our chili carne, cheddar cheese, jalapeno, honey mustard**Lava fries 1.500 OMRTopped with fried bacon, fried onion, cheddar cheese, ranch sauce*Sides**Crispy strips 1.800 OMR5 pieces of chicken strips topped with BBQ sauce or honey mustard sauce, Wurmelo side sauce**Jalapeno cheese balls 1.300 OMR6 pieces of jalapeno cheese balls, sweet chili side sauce**Nachos 1.500 OMRA plate of nachos topped with cheddar cheese and jalapeno*Drinks**Flavored sparkling cans 0.800 OMR **Fresh orange juice 1.400 OMR**Mineral water 0.300 OMR**Soft drink 0.400 OMR**Mojito 1.500 OMRThe menu should not have any of our products pictures (icons/symbols proffered). we would prefer if the designs have unique icons/symbols created for Wurmelo. you can check our Instagram page https://www.snapfolio.example/wurmelo.official/

Industry/Entity Type

American Restaurant

Colors

Designer to choose colors to be used in the design.

Requirements
Must have
• Wurmelo Logo, Icons

```html
<!DOCTYPE html>
<html lang="en">
<head>
<meta charset="utf-8">
<title>Wurmelo Menu</title>
<link href="https://fonts.googleapis.com/css2?family=Oswald:wght@500;700&family=Roboto+Slab:wght@700&family=Open+Sans:wght@400;600&display=swap" rel="stylesheet">
<style>
  :root{
    --bg:#131212;
    --bg-soft:#211f1f;
    --frame:#c8161d;
    --yellow:#f5c400;
    --white:#ffffff;
    --muted:#b9b4b0;
    --leader:#6b6663;
  }
  *{margin:0;padding:0;box-sizing:border-box}
  html,body{width:857px;height:1200px;overflow:hidden;background:var(--bg)}
  .menu{
    position:relative;width:857px;height:1200px;
    background:radial-gradient(ellipse at 50% 40%,var(--bg-soft) 0%,var(--bg) 70%);
    color:var(--white);font-family:"Open Sans",sans-serif;
  }
  .frame{position:absolute;inset:0}
  .brand{
    position:absolute;top:24px;left:0;right:0;
    display:flex;justify-content:center;align-items:center;gap:10px;
  }
  .brand-dot{width:16px;height:16px;border-radius:50%;background:var(--frame)}
  .brand-name{font-family:"Oswald",sans-serif;font-weight:700;font-size:44px;color:var(--yellow);letter-spacing:2px;text-transform:uppercase}
  .title{
    position:absolute;top:112px;left:0;right:0;text-align:center;
    font-family:"Oswald",sans-serif;font-weight:700;font-size:42px;letter-spacing:3px;
  }
  .col{position:absolute;top:188px}
  .col-left{left:56px;width:350px}
  .col-right{left:446px;width:356px}
  .section{font-family:"Oswald",sans-serif;font-weight:700;font-size:30px;line-height:1.1;letter-spacing:1px}
  .group{font-family:"Oswald",sans-serif;font-weight:700;font-size:34px;color:var(--yellow);line-height:1.1;letter-spacing:1px}
  .group-note{font-size:11.5px;color:var(--muted);line-height:1.45;margin:6px 0 18px}
  .item{margin-bottom:16px}
  .item-row{display:flex;align-items:baseline;gap:6px}
  .item-name{font-family:"Roboto Slab",serif;font-weight:700;font-size:18px;white-space:nowrap}
  .leader{flex:1;border-bottom:2px dotted var(--leader);transform:translateY(-4px)}
  .price{font-size:14px;font-weight:600;white-space:nowrap}
  .item-desc{font-size:11.5px;color:var(--muted);line-height:1.4;margin-top:3px}
  .col-right .item{margin-bottom:14px}
  .col-right .item-name{font-size:20px}
  .col-right .section{margin-bottom:14px}
  .spacer{height:22px}
  .dots{position:absolute;top:1052px;left:0;right:0;text-align:center;letter-spacing:8px;color:var(--white);font-size:12px}
  .toppings-title{position:absolute;top:1068px;left:0;right:0;text-align:center;font-family:"Oswald",sans-serif;font-weight:700;font-size:32px;color:var(--yellow);letter-spacing:1px}
  .toppings{position:absolute;top:1112px;left:170px;right:170px;display:flex;justify-content:space-between}
  .topping{width:110px;text-align:center;font-size:11.5px;line-height:1.3}
  .topping-art{width:62px;height:36px;margin:0 auto 6px;border-radius:50%}
  .art-veg{background:linear-gradient(#7dbb3b,#3f7d21)}
  .art-cheese{background:linear-gradient(#ffd84a,#e8a800);border-radius:6px}
  .art-patty{background:linear-gradient(#8a5430,#4a2b16)}
  .art-bacon{background:linear-gradient(#f0a090,#c0483a);border-radius:6px}
</style>
</head>
<body>
<main class="menu">
  <svg class="frame" width="857" height="1200" viewBox="0 0 857 1200" aria-hidden="true">
    <rect x="16" y="16" width="825" height="1168" fill="none" stroke="var(--frame)" stroke-width="2"/>
    <rect x="26" y="26" width="805" height="1148" fill="none" stroke="var(--frame)" stroke-width="1"/>
    <path d="M16 70 H60 V16 M841 70 H797 V16 M16 1130 H60 V1184 M841 1130 H797 V1184" fill="none" stroke="var(--frame)" stroke-width="2"/>
  </svg>

  <header class="brand">
    <span class="brand-dot"></span>
    <span class="brand-name">Wurmelo</span>
  </header>
  <h1 class="title">MENÜ</h1>

  <section class="col col-left">
    <h2 class="section">SANDWICHES</h2>
    <h3 class="group">HOTDOGS</h3>
    <p class="group-note">Our special fresh grilled hotdog served on fresh buns<br>(Regular - 1.300 OMR / Franks - 2.000 OMR)</p>

    <div class="item"><div class="item-row"><span class="item-name">Wurmelo</span><span class="leader"></span></div>
      <p class="item-desc">Lettuce, tomato, jalapeno, pickle, onion, corn, chips, cheese, ketchup, mayo, mustard</p></div>
    <div class="item"><div class="item-row"><span class="item-name">Pepper</span><span class="leader"></span></div>
      <p class="item-desc">Bell pepper, onion, sweet chili sauce, avocado</p></div>
    <div class="item"><div class="item-row"><span class="item-name">Chili Flames</span><span class="leader"></span></div>
      <p class="item-desc">Chili carne, cheddar cheese, honey mustard</p></div>
    <div class="item"><div class="item-row"><span class="item-name">Chicago</span><span class="leader"></span></div>
      <p class="item-desc">Tomato, pickle, red onion, sweet relish, mustard</p></div>
    <div class="item"><div class="item-row"><span class="item-name">New York</span><span class="leader"></span></div>
      <p class="item-desc">Grilled onion, beef bacon, barbecue sauce, chili mustard</p></div>
    <div class="item"><div class="item-row"><span class="item-name">Egg &amp; Cheese</span><span class="leader"></span></div>
      <p class="item-desc">Omelet, cheese, ketchup, mayo, mustard</p></div>

    <h3 class="group" style="margin-top:22px">BURGERS</h3>
    <p class="group-note">100% all natural beef &amp; freshly ground,<br>100 grams each patty served on fresh buns.<br>(Single patty - 2.000 OMR / double patty - 2.500 OMR)</p>

    <div class="item"><div class="item-row"><span class="item-name">Sweet Beef Burger</span><span class="leader"></span></div>
      <p class="item-desc">Beef bacon, cheese, lettuce, tomato, pickle.</p></div>
    <div class="item"><div class="item-row"><span class="item-name">Cheese Beef Burger</span><span class="leader"></span></div>
      <p class="item-desc">Cheese, pickle, Wurmelo sauce.</p></div>
    <div class="item"><div class="item-row"><span class="item-name">Mexican Beef Burger</span><span class="leader"></span></div>
      <p class="item-desc">Guacamole sauce, red onion, lettuce, tomato, Wurmelo sauce</p></div>
    <div class="item"><div class="item-row"><span class="item-name">Chicken Burger</span><span class="leader"></span></div>
      <p class="item-desc">Fried chicken patty, lettuce, tomato, ranch sauce, Wurmelo sauce</p></div>
  </section>

  <section class="col col-right">
    <h2 class="section">FRIES</h2>
    <div class="item"><div class="item-row"><span class="item-name">Regular</span><span class="leader"></span><span class="price">0.600 OMR</span></div></div>
    <div class="item"><div class="item-row"><span class="item-name">Crispy</span><span class="leader"></span><span class="price">0.800 OMR</span></div></div>
    <div class="item"><div class="item-row"><span class="item-name">Wedges</span><span class="leader"></span><span class="price">0.800 OMR</span></div></div>
    <div class="item"><div class="item-row"><span class="item-name">Chili fries</span><span class="leader"></span><span class="price">1.500 OMR</span></div>
      <p class="item-desc">Topped with our chili carne, cheddar cheese,<br>jalapeno, honey mustard</p></div>
    <div class="item"><div class="item-row"><span class="item-name">Lava fries</span><span class="leader"></span><span class="price">1.500 OMR</span></div>
      <p class="item-desc">Topped with fried bacon, fried onion,<br>cheddar cheese, ranch sauce</p></div>

    <div class="spacer"></div>
    <h2 class="section">SIDES</h2>
    <div class="item"><div class="item-row"><span class="item-name">Crispy strips</span><span class="leader"></span><span class="price">1.800 OMR</span></div>
      <p class="item-desc">5 pieces of chicken strips topped with BBQ sauce<br>or honey mustard sauce, Wurmelo side sauce</p></div>
    <div class="item"><div class="item-row"><span class="item-name">Jalapeno cheese balls</span><span class="leader"></span><span class="price">1.300 OMR</span></div>
      <p class="item-desc">6 pieces of jalapeno cheese balls,<br>sweet chili side sauce</p></div>
    <div class="item"><div class="item-row"><span class="item-name">Nachos</span><span class="leader"></span><span class="price">1.500 OMR</span></div>
      <p class="item-desc">A plate of nachos topped with<br>cheddar cheese and jalapeno</p></div>

    <div class="spacer"></div>
    <h2 class="section">DRINKS</h2>
    <div class="item"><div class="item-row"><span class="item-name">Flavored sparkling cans</span><span class="leader"></span><span class="price">0.800 OMR</span></div></div>
    <div class="item"><div class="item-row"><span class="item-name">Fresh orange juice</span><span class="leader"></span><span class="price">1.400 OMR</span></div></div>
    <div class="item"><div class="item-row"><span class="item-name">Mineral water</span><span class="leader"></span><span class="price">0.300 OMR</span></div></div>
    <div class="item"><div class="item-row"><span class="item-name">Soft drink</span><span class="leader"></span><span class="price">0.400 OMR</span></div></div>
    <div class="item"><div class="item-row"><span class="item-name">Mojito</span><span class="leader"></span><span class="price">1.500 OMR</span></div></div>
  </section>

  <div class="dots" aria-hidden="true">● ● ● ● ● ● ● ● ● ● ● ● ● ● ●</div>
  <h2 class="toppings-title">TOPPINGS</h2>
  <div class="toppings">
    <div class="topping"><div class="topping-art art-veg" role="img" aria-label="Illustration of fresh vegetables"></div>Extra veggies<br>0.100 OMR</div>
    <div class="topping"><div class="topping-art art-cheese" role="img" aria-label="Illustration of a cheese wedge"></div>Extra cheese<br>0.200 OMR</div>
    <div class="topping"><div class="topping-art art-patty" role="img" aria-label="Illustration of a beef patty"></div>Extra patty<br>0.500 OMR</div>
    <div class="topping"><div class="topping-art art-bacon" role="img" aria-label="Illustration of beef bacon strips"></div>Extra beef Bacon<br>0.400 OMR</div>
  </div>
</main>
</body>
</html>
```